Virtual Reality immersive experiences

Print ad 8.5" X 11"
Advertising to have people come rent time in our virtual reality room.
Fun for all ages
Unique experience
Immersive experience into 3D world
Escape reality
Be at heart of action - bottom of the ocean, travel the world, fight the invaders, solve the mystery and so much more
System used is Brelvo Optra
Dedicated room
Family friendly
$24 half hour
$40 per hour
Updates

Industry/Entity Type

Advertising

Requirements
Must have
• Be fun looking
• Eye catching
• Great pictures of VR experiences
• Pricing is $24 / 30 minutes and $40 / 1 hour
• Our location: 587 Larch Avenue, Three Hills, Alberta
• Our contact: 403-618-2093
• I have attached TERMALDO Technology Solutions logo which should be somewhere on the ad.
Nice to have
• could use phrases like: travel the world, explore the ocean depths, fight the invaders, visit the carnival

```html
<!DOCTYPE html>
<html lang="en">
<head>
<meta charset="utf-8">
<title>TERMALDO VR Experience Ad</title>
<link href="https://fonts.googleapis.com/css2?family=Bebas+Neue&family=Open+Sans:wght@400;600&family=Roboto+Condensed:wght@700&display=swap" rel="stylesheet">
<style>
  :root {
    --page-bg: #e6e6e6;
    --sky-blue: #13b4ee;
    --deep-blue: #0a8fd6;
    --charcoal: #2e2e30;
    --ink: #222222;
    --white: #ffffff;
    --mist: #eeeeee;
  }
  html, body {
    margin: 0;
    width: 825px;
    height: 1200px;
    overflow: hidden;
    background: var(--page-bg);
  }
  .flyer {
    position: absolute;
    left: 105px;
    top: 188px;
    width: 640px;
    height: 827px;
    overflow: hidden;
    background: var(--mist);
    font-family: "Open Sans", sans-serif;
  }
  .flyer-shapes { position: absolute; inset: 0; }
  .brand {
    position: absolute;
    left: 38px;
    top: 30px;
    width: 240px;
    text-align: center;
    color: var(--deep-blue);
    font-family: "Roboto Condensed", sans-serif;
    font-weight: 700;
    line-height: 1;
  }
  .brand-name { font-size: 44px; letter-spacing: 1px; }
  .brand-sub { font-size: 12.5px; letter-spacing: 1.4px; margin-top: 3px; text-transform: uppercase; }
  .tagline {
    position: absolute;
    left: 48px;
    top: 98px;
    margin: 0;
    font-size: 14px;
    line-height: 19.5px;
    color: var(--ink);
  }
  .tagline span { display: block; white-space: nowrap; }
  .join-badge {
    position: absolute;
    left: 245px;
    top: 225px;
    width: 150px;
    text-align: center;
    color: var(--white);
    font-family: "Roboto Condensed", sans-serif;
    font-weight: 700;
    line-height: 0.95;
  }
  .join-badge span { display: block; }
  .join-top { font-size: 44px; }
  .join-bottom { font-size: 66px; }
  .price {
    position: absolute;
    top: 297px;
    font-family: "Roboto Condensed", sans-serif;
    font-weight: 700;
    font-size: 35.5px;
    line-height: 40px;
    margin: 0;
  }
  .price-amount { color: var(--sky-blue); display: block; }
  .price-unit { color: var(--white); display: block; }
  .price-half { left: 43px; }
  .price-full { right: 31px; text-align: left; }
  .contact-line {
    position: absolute;
    left: 60px;
    top: 411px;
    margin: 0;
    color: var(--white);
    font-family: "Roboto Condensed", sans-serif;
    font-weight: 700;
    font-size: 26.5px;
    white-space: nowrap;
  }
  .headline {
    position: absolute;
    right: 32px;
    top: 483px;
    margin: 0;
    text-align: right;
    font-family: "Bebas Neue", sans-serif;
    font-weight: 400;
    line-height: 1;
  }
  .headline-lead { display: block; font-size: 40px; color: var(--ink); }
  .headline-main { display: block; font-size: 78px; color: var(--deep-blue); margin-top: -4px; }
  .features {
    position: absolute;
    left: 38px;
    top: 611px;
    margin: 0;
    padding: 0;
    list-style: none;
    font-size: 19px;
    line-height: 27.2px;
    color: var(--ink);
  }
  .features li { position: relative; padding-left: 28px; white-space: nowrap; }
  .features li::before {
    content: "";
    position: absolute;
    left: 0;
    top: 8px;
    width: 12px;
    height: 12px;
    border-radius: 50%;
    background: var(--sky-blue);
  }
  .address {
    position: absolute;
    right: 40px;
    top: 786px;
    margin: 0;
    color: var(--white);
    font-size: 16.5px;
    font-weight: 600;
    letter-spacing: 0.3px;
  }
</style>
</head>
<body>
<main class="flyer">
  <svg class="flyer-shapes" width="640" height="827" viewBox="0 0 640 827">
    <defs>
      <linearGradient id="sky" x1="0" y1="0" x2="0" y2="1">
        <stop offset="0" stop-color="#6fb8f0"/>
        <stop offset="0.6" stop-color="#cfe4f3"/>
        <stop offset="1" stop-color="#f4f6f8"/>
      </linearGradient>
      <linearGradient id="lower-mist" x1="0" y1="0" x2="1" y2="1">
        <stop offset="0" stop-color="#d9d9d9"/>
        <stop offset="1" stop-color="#f4f4f4"/>
      </linearGradient>
      <linearGradient id="headset" x1="0" y1="0" x2="1" y2="1">
        <stop offset="0" stop-color="#3a3a3a"/>
        <stop offset="1" stop-color="#111111"/>
      </linearGradient>
      <linearGradient id="badge" x1="0" y1="0" x2="0" y2="1">
        <stop offset="0" stop-color="#2cc3f5"/>
        <stop offset="1" stop-color="#0a93d9"/>
      </linearGradient>
    </defs>

    <rect class="lower-backdrop" role="img" aria-label="Faded photo of a family enjoying virtual reality" x="0" y="430" width="640" height="397" fill="url(#lower-mist)"/>

    <rect x="0" y="0" width="303" height="220" fill="#f6f6f6"/>

    <polygon role="img" aria-label="Photo of a joyful woman with arms raised against a blue sky" points="323,0 640,0 640,168 323,292" fill="url(#sky)"/>

    <rect x="303" y="0" width="12" height="185" fill="var(--charcoal)"/>

    <polygon points="0,180 320,300 640,186 640,460 0,460" fill="var(--charcoal)"/>
    <polygon points="0,162 320,280 320,298 0,180" fill="var(--sky-blue)"/>
    <polygon points="640,164 320,280 320,298 640,182" fill="var(--sky-blue)"/>

    <polygon points="0,460 450,460 0,548" fill="var(--white)"/>
    <polygon points="0,548 470,456 470,462 0,575" fill="var(--sky-blue)"/>
    <polygon points="0,575 470,462 470,466 0,584" fill="var(--white)"/>

    <polygon points="48,400 640,400 640,458 28,458" fill="var(--sky-blue)"/>

    <rect x="250" y="212" width="140" height="140" rx="30" ry="30" transform="rotate(45 320 282)" fill="url(#badge)" stroke="var(--white)" stroke-width="6"/>

    <rect role="img" aria-label="Photo of a black virtual reality headset" x="345" y="612" width="245" height="140" rx="40" fill="url(#headset)"/>

    <path d="M0,794 L250,794 C275,794 280,754 310,754 L640,754 L640,760 L312,760 C286,760 280,800 252,800 L0,800 Z" fill="#3a3a3a"/>
    <path d="M0,800 L252,800 C280,800 286,760 312,760 L640,760 L640,827 L0,827 Z" fill="var(--sky-blue)"/>
  </svg>

  <header class="brand">
    <div class="brand-name">TERMALDO</div>
    <div class="brand-sub">Technology Solutions</div>
  </header>

  <p class="tagline"><span>Be at heart of action - bottom</span><span>of the ocean, travel the world,</span><span>fight the invaders, solve the</span><span>mystery and so much more</span></p>

  <div class="join-badge"><span class="join-top">JOIN</span><span class="join-bottom">US!</span></div>

  <p class="price price-half"><span class="price-amount">$24 HALF</span><span class="price-unit">PER HOUR</span></p>
  <p class="price price-full"><span class="price-amount">$40 PER</span><span class="price-unit">PER HOUR</span></p>

  <p class="contact-line">Contact us to know more about us at: 403-618-2093</p>

  <h1 class="headline"><span class="headline-lead">Immersive Experience</span><span class="headline-main">Into 3D World</span></h1>

  <ul class="features">
    <li>Fun for all ages</li>
    <li>Unique experience</li>
    <li>Escape reality</li>
    <li>System used is Brelvo Optra</li>
    <li>Dedicated room</li>
    <li>Family friendly</li>
  </ul>

  <p class="address">587 Larch Avenue, Three Hills, Alberta</p>
</main>
</body>
</html>
```